新しくオープンしたラーメン居酒屋の新メニューのチラシ制作をお願いします。
こだわりが強く、比較的高級なラーメン屋です。高級感のある本格的なデザイン、訴求力がありながらも上品なデザインを希望します。
サイズ:A4サイズ
ノビテルで入稿します。
編集できるイラストレーターとPDFファイルでの納品をお願いします。

イメージ通りでした。

この度はたくさんのご応募ありがとうございます。今後ともよろしくお願いいたします。

```html
<!DOCTYPE html>
<html lang="ja">
<head>
<meta charset="utf-8">
<title>夏季限定 冷製・鯛出汁塩山椒そば</title>
<link href="https://fonts.googleapis.com/css2?family=Shippori+Mincho:wght@500;700&display=swap" rel="stylesheet">
<style>
:root{
  --paper:#efefec;
  --green:#3d5a3a;
  --ink:#3f5a3c;
  --text:#3a3a36;
  --bowl-light:#f6b26a;
  --bowl-dark:#dd8a36;
  --herb:#7f9a6a;
}
*{margin:0;padding:0;box-sizing:border-box}
html,body{width:849px;height:1200px;overflow:hidden;background:var(--paper)}
.flyer{position:relative;width:849px;height:1200px;overflow:hidden;
  background:radial-gradient(circle at 70% 30%,#f7f7f5,var(--paper) 70%);
  font-family:"Shippori Mincho",serif;color:var(--text)}
.side-band{position:absolute;left:0;top:0;width:270px;height:750px;background:var(--green)}
.bowl-photo{position:absolute;left:50px;top:438px;width:568px;height:568px;border-radius:50%;
  background:radial-gradient(circle at 50% 50%,#f3ece0 0 30%,var(--bowl-light) 42%,var(--bowl-dark) 100%);
  box-shadow:0 14px 30px rgba(0,0,0,.18)}
.herb-photo{position:absolute;right:0;bottom:0;width:220px;height:270px;
  background:radial-gradient(ellipse at 60% 65%,var(--herb),rgba(127,154,106,0) 70%)}
.vertical{position:absolute;writing-mode:vertical-rl}
.season{right:58px;top:40px;font-size:26px;font-weight:500;color:var(--ink);letter-spacing:.12em}
.dish-name{right:78px;top:185px;font-size:56px;font-weight:700;color:var(--ink);letter-spacing:.08em;line-height:1}
.lead{right:200px;top:113px;font-size:16px;line-height:2.3;letter-spacing:.12em;height:380px}
.note{position:absolute;left:40px;top:1076px;font-size:14px;color:var(--ink)}
.price{position:absolute;left:40px;top:1106px;font-size:32px;color:var(--ink);letter-spacing:.04em}
</style>
</head>
<body>
<div class="flyer">
  <div class="side-band"></div>
  <div class="bowl-photo" role="img" aria-label="鯛出汁の冷製塩山椒そば、海老とトマトをのせたオレンジの器"></div>
  <div class="herb-photo" role="img" aria-label="青山椒の実の枝"></div>

  <p class="vertical season">夏季限定</p>
  <h1 class="vertical dish-name">冷製・鯛出汁塩山椒そば</h1>
  <p class="vertical lead">濃密ながら後味爽やかな真鯛出汁。<br>香りの異なる２種類の<br>山椒を効かせた香味油。<br>自家製の麺だからこそ<br>三位一体となった一杯。</p>

  <p class="note">化学調味料不使用</p>
  <p class="price">¥ 1,000</p>
</div>
</body>
</html>
```